Professional Shoeshine Postcard Design

Mr. Garrick Professional Shoeshine offers Stand Service, Drop Off Service, and mobile service. I shine shoes, boots, purses, leather brief cases, all leather goods. (See Attachments) "HOW'S YOUR IMAGE" should headline the post card. Please use stock pics available to you of nicely polished leather boots purses etc. Card can be two sides to get in info. Card should be 5x7.

```html
<!DOCTYPE html>
<html lang="en">
<head>
<meta charset="utf-8">
<title>Mr. Garrick Professional Shoeshine – Postcard</title>
<link rel="stylesheet" href="https://fonts.googleapis.com/css2?family=Oswald:wght@500;700&family=Cinzel:wght@700&family=Open+Sans:wght@400;600;700&display=swap">
<style>
:root{
  --orange:#f26a10;
  --orange-deep:#d9530a;
  --orange-light:#f8962e;
  --ink:#5a5a5a;
  --ink-dark:#3b3b3b;
  --brown:#4a2a12;
  --cream:#fff3c4;
  --white:#ffffff;
  --page:#e9e7e4;
}
*{box-sizing:border-box;margin:0;padding:0}
html,body{width:863px;height:1200px;overflow:hidden;background:var(--page)}
body{position:relative;font-family:'Open Sans',Arial,sans-serif}
.card{position:absolute;left:41px;width:780px;height:557px;background:var(--white);overflow:hidden;box-shadow:0 4px 14px rgba(0,0,0,.18)}
.card--front{top:28px}
.card--back{top:615px}

/* front */
.portrait-photo{position:absolute;left:320px;top:0;width:460px;height:330px;background:linear-gradient(90deg,rgba(255,255,255,1) 0%,#e8ddd0 30%,#c9b49a 65%,#8f7c68 100%)}
.headline{position:absolute;left:30px;top:14px;font-family:'Oswald',Arial,sans-serif;font-weight:700;line-height:.95;text-transform:uppercase}
.headline__top{display:block;font-size:60px;color:var(--orange)}
.headline__main{display:block;font-size:124px;color:var(--ink);letter-spacing:1px}
.swoosh{position:absolute;left:0;top:0;width:780px;height:557px}
.brand{position:absolute;left:40px;top:292px;color:var(--white)}
.brand__name{font-family:'Cinzel',Georgia,serif;font-size:46px;letter-spacing:1px;line-height:1}
.brand__tag{font-family:'Oswald',Arial,sans-serif;font-weight:500;font-size:23px;letter-spacing:1px;margin-top:4px}
.goods{position:absolute;left:0;top:398px;width:780px;height:34px;background:var(--white);display:flex;align-items:center;padding-left:40px;gap:10px;font-family:'Oswald',Arial,sans-serif;font-weight:500;font-size:17px;color:var(--orange-deep)}
.goods__sep{color:var(--ink)}
.call-band{position:absolute;left:0;top:432px;width:780px;height:125px;background:linear-gradient(180deg,var(--orange) 0%,var(--orange-deep) 100%);display:flex;align-items:center;justify-content:space-between;padding:0 30px 0 40px}
.call-band__text{font-family:'Oswald',Arial,sans-serif;font-weight:700;font-size:38px;color:var(--white)}
.call-band__phone{background:var(--white);border-radius:10px;padding:8px 22px;font-family:'Oswald',Arial,sans-serif;font-weight:700;font-size:38px;color:var(--ink-dark)}

/* back */
.info-panel{position:absolute;left:0;top:0;width:395px;height:557px;background:linear-gradient(180deg,var(--orange-light) 0%,var(--orange) 100%)}
.panel-title{position:absolute;left:0;width:395px;height:28px;background:var(--orange-deep);color:var(--white);font-family:'Oswald',Arial,sans-serif;font-weight:700;font-size:18px;line-height:28px;padding-left:22px;letter-spacing:.5px}
.bullet-list{position:absolute;display:grid;grid-template-columns:190px 170px;column-gap:6px;row-gap:2px;list-style:none;color:var(--white);font-size:12.5px;font-weight:600;line-height:1.25}
.bullet-list li{padding-left:12px;position:relative}
.bullet-list li::before{content:"";position:absolute;left:0;top:6px;width:5px;height:5px;background:var(--cream);border-radius:50%}
.tagline-strip{position:absolute;left:0;top:196px;width:395px;height:26px;background:var(--brown);color:var(--cream);font-family:'Oswald',Arial,sans-serif;font-weight:500;font-size:12.5px;line-height:26px;padding-left:14px;letter-spacing:.3px;white-space:nowrap}
.shoe-photo{position:absolute;top:232px;height:96px;border:3px solid var(--white);border-radius:4px}
.shoe-photo--before{left:22px;width:140px;background:linear-gradient(135deg,#8a8070,#c9c0b0 60%,#6f6558)}
.shoe-photo--after{left:208px;width:168px;background:linear-gradient(135deg,#5a2a10,#b8642a 55%,#3a1a08)}
.shoe-label{position:absolute;top:310px;font-family:'Oswald',Arial,sans-serif;font-weight:700;font-size:12px;color:var(--white)}
.arrow{position:absolute;left:168px;top:262px}
.contact-row{position:absolute;left:22px;top:518px;display:flex;gap:28px;color:var(--white);font-weight:700;font-size:14px;align-items:center}
.contact-row span{display:flex;align-items:center;gap:6px}

.stamp-box{position:absolute;left:650px;top:28px;width:100px;height:110px;border:2px solid #9a9a9a}
.address-lines{position:absolute;left:440px;top:370px;width:310px}
.address-lines div{height:1px;background:#9a9a9a;margin-bottom:40px}
</style>
</head>
<body>

<section class="card card--front">
  <div class="portrait-photo" role="img" aria-label="Photo of a smiling older gentleman in a sweater holding a shoe at a shine stand"></div>
  <h1 class="headline"><span class="headline__top">How's Your</span><span class="headline__main">Image</span></h1>
  <svg class="swoosh" viewBox="0 0 780 557" aria-hidden="true">
    <defs>
      <linearGradient id="swooshFill" x1="0" y1="0" x2="0" y2="1">
        <stop offset="0" stop-color="#f8962e"/>
        <stop offset="1" stop-color="#e85d0c"/>
      </linearGradient>
    </defs>
    <path d="M0,255 C240,300 520,250 780,190 L780,400 L0,400 Z" fill="#b9b9b9"/>
    <path d="M0,268 C240,312 520,262 780,204 L780,400 L0,400 Z" fill="#ffffff"/>
    <path d="M0,282 C250,322 520,282 780,226 L780,400 L0,400 Z" fill="url(#swooshFill)"/>
  </svg>
  <div class="brand">
    <div class="brand__name">MR. GARRICK</div>
    <div class="brand__tag">PROFESSIONAL SHOESHINE</div>
  </div>
  <div class="goods">
    <span>SHOES</span><span class="goods__sep">|</span>
    <span>BOOTS</span><span class="goods__sep">|</span>
    <span>HANDBAGS</span><span class="goods__sep">|</span>
    <span>BRIEFCASES</span><span class="goods__sep">|</span>
    <span>JACKETS/COATS</span>
  </div>
  <div class="call-band">
    <div class="call-band__text">CALL MR. GARRICK HOLLIS</div>
    <div class="call-band__phone">555 014-2297</div>
  </div>
</section>

<section class="card card--back">
  <div class="info-panel">
    <div class="panel-title" style="top:22px">STAND SERVICE</div>
    <ul class="bullet-list" style="left:22px;top:58px">
      <li>Trade Shows/Conferences</li><li>Team Building Events</li>
      <li>Cocktail Parties</li><li>Exhibitions</li>
      <li>Receptions</li><li>Openings/Launchings</li>
      <li>Promotions</li><li>Office Building Lobby</li>
      <li>Corporate Functions and Meetings</li><li>Drop off Pick Up</li>
    </ul>
    <div class="tagline-strip">FROM THE IMPOSSIBLE &nbsp;&gt;&nbsp; TO THE INCREDIBLE &nbsp;&gt;&nbsp; TO THE BEAUTIFUL</div>
    <div class="shoe-photo shoe-photo--before" role="img" aria-label="Worn, scuffed leather shoe before shining"></div>
    <div class="shoe-label" style="left:32px">BEFORE</div>
    <svg class="arrow" width="34" height="36" viewBox="0 0 34 36" aria-hidden="true"><path d="M2,10 H18 V2 L32,18 L18,34 V26 H2 Z" fill="#ffffff"/></svg>
    <div class="shoe-photo shoe-photo--after" role="img" aria-label="Glossy polished brown leather shoe after shining"></div>
    <div class="shoe-label" style="left:218px">AFTER</div>
    <div class="panel-title" style="top:344px">STAND SERVICE</div>
    <ul class="bullet-list" style="left:22px;top:382px">
      <li>Keystone Bank</li><li>Grand Crescent Hotel</li>
      <li>Nat'l Assoc of Home Crafters</li><li>Marlow Wardell Park Hotel</li>
      <li>Life Assurance Partners, Inc.</li><li>Capitol Linden Hotel</li>
    </ul>
    <div class="contact-row">
      <span><svg width="14" height="14" viewBox="0 0 24 24" aria-hidden="true"><path d="M6.6 10.8a15 15 0 0 0 6.6 6.6l2.2-2.2a1 1 0 0 1 1-.25 11.4 11.4 0 0 0 3.6.6 1 1 0 0 1 1 1V20a1 1 0 0 1-1 1A17 17 0 0 1 3 4a1 1 0 0 1 1-1h3.5a1 1 0 0 1 1 1c0 1.25.2 2.45.6 3.6a1 1 0 0 1-.25 1z" fill="#ffffff"/></svg>555 014-2297</span>
      <span><svg width="16" height="12" viewBox="0 0 16 12" aria-hidden="true"><rect x="0.5" y="0.5" width="15" height="11" fill="none" stroke="#ffffff"/><path d="M0.5,0.5 L8,7 L15.5,0.5" fill="none" stroke="#ffffff"/></svg>mrgarrickdc@mailbox.com</span>
    </div>
  </div>
  <div class="stamp-box"></div>
  <div class="address-lines"><div></div><div></div><div></div><div></div></div>
</section>

</body>
</html>
```